Redesign Of Hotel Coupon/Voucher 8.5 x 11

I would like to redesign my voucher.

Please provide me a color flyer design but one that would be easy on printing costs...for example printing from home computer/printer.

I would like to see some color designs...maybe some black and white and also full graphics and even basic like the plum tally voucher I provided as a sample. The 2 night hotel stay is the voucher I need to redesign...

Target Market(s)

Consumers

Industry/Entity Type

Hotel

Requirements
Must have
• exact text in current designs---look official, credible and trust worthy
Nice to have
• I would like to redesign my voucher.
• Please provide me a color flyer design but one that would be easy on printing costs...for example printing from home computer/printer.
• I would like to see some color designs...maybe some black and white and also full graphics and even basic like the plum tally voucher I provided as a sample. The 2 night hotel stay is the voucher I need to redesign...
Should not have

```html
<!DOCTYPE html>
<html lang="en">
<head>
<meta charset="utf-8">
<title>2 Night Hotel Stay Certificate</title>
<link rel="stylesheet" href="https://fonts.googleapis.com/css2?family=Roboto+Condensed:wght@400;700&family=Fira+Sans+Extra+Condensed:wght@400;500;600&display=swap">
<style>
:root{
  --backdrop:#e9e6e1;
  --paper:#ffffff;
  --ink:#1d1d1d;
  --orange:#f47b20;
  --title-orange:#f26522;
  --legend:#c4842c;
  --teal:#2a98ae;
  --red:#c0262d;
  --panel:#f4f4f4;
  --rule:#8a8a8a;
  --link:#1f63c8;
}
*{box-sizing:border-box;margin:0;padding:0}
html,body{width:1200px;height:1200px;overflow:hidden;background:var(--backdrop)}
.stage{position:relative;width:1200px;height:1200px;overflow:hidden}
.flyer{position:absolute;left:145px;top:10px;width:1018px;height:1320px;background:var(--paper);
  transform:scale(.894);transform-origin:0 0;box-shadow:0 2px 10px rgba(0,0,0,.18);
  font-family:"Fira Sans Extra Condensed",sans-serif;color:var(--ink)}
.hero{position:absolute;left:37px;top:37px;width:944px;height:414px;border-radius:6px;overflow:hidden;border:1px solid #555}
.hero-photo{position:absolute;inset:0;background:
  radial-gradient(ellipse at 80% 10%,rgba(255,214,150,.85),transparent 45%),
  radial-gradient(ellipse at 45% 75%,rgba(236,200,120,.7),transparent 40%),
  linear-gradient(160deg,#7d8fa5 0%,#4a5262 40%,#2a2c36 75%,#1c1d25 100%)}
.hero-title{position:absolute;left:21px;top:334px;font-family:"Roboto Condensed",sans-serif;font-weight:700;font-size:58px;color:#fff;
  letter-spacing:.5px;text-shadow:0 2px 6px rgba(0,0,0,.6)}
.hero-title .nights{color:var(--title-orange)}
.gift-note{position:absolute;left:723px;top:203px;width:210px;height:203px}
.gift-note svg{position:absolute;inset:0}
.gift-note-text{position:absolute;inset:14px 6px 0;text-align:center;color:var(--red);font-family:"Roboto Condensed",sans-serif;font-weight:700;font-size:22px;line-height:26px}
.gift-note-text .fields{margin-top:12px}
.boxed{position:absolute;left:37px;width:944px;border:1.5px solid #333;border-radius:5px;padding:13px 12px 6px}
.boxed .legend{position:absolute;left:8px;top:-12px;background:var(--paper);padding:0 4px;color:var(--legend);font-weight:600;font-size:19px;line-height:20px}
.boxed p{font-size:12.4px;line-height:17.6px;text-align:justify;letter-spacing:-.25px}
.destinations{top:479px;height:111px}
.terms{top:611px;height:284px}
.order{position:absolute;left:37px;top:910px;width:944px;height:336px;background:var(--panel);border:1px solid #aaa;border-radius:5px}
.redeem{position:absolute;left:7px;top:9px;width:310px;height:318px;background:var(--paper);border:1.5px solid #222;border-radius:5px;padding:12px 9px 0 9px;font-size:13px;line-height:18px;letter-spacing:-.15px}
.redeem .intro{text-align:justify}
.redeem h3{color:var(--teal);font-weight:400;font-size:13.5px;margin:10px 0 8px}
.redeem .step{margin-bottom:4px}
.redeem .url{color:var(--link);padding-left:10px;margin-bottom:8px}
.redeem .addr{padding-left:10px;margin-bottom:8px}
.redeem .meta{display:grid;grid-template-columns:93px auto;font-weight:600}
.redeem .meta .val{font-weight:500}
.redeem .meta .expiry{color:var(--red)}
.form-col{position:absolute;top:22px;font-size:13.5px}
.billing{left:339px;width:306px}
.payment{left:665px;width:266px}
.form-col h4{color:var(--teal);font-weight:400;font-size:14px;margin-bottom:3px;letter-spacing:.2px}
.row{display:flex;align-items:flex-end;height:18px}
.row .lab{flex:0 0 auto;width:48px;white-space:nowrap}
.row .line{flex:1;border-bottom:1px solid var(--rule);margin-bottom:4px}
.shipping-head{margin-top:14px}
.payment .row .lab{width:auto;min-width:86px;margin-right:4px}
.method-title{margin:2px 0 6px}
.methods{display:grid;grid-template-columns:138px auto;row-gap:0;margin-bottom:14px}
.methods span{display:flex;align-items:center;height:18px}
.methods span::before{content:"";width:9px;height:9px;border:1px solid #333;margin-right:7px;background:#fff}
.expiry-row .short{flex:0 0 30px;border-bottom:1px solid var(--rule);margin-bottom:4px}
.expiry-row .slash{margin:0 3px}
.agree{margin-top:9px}
.payment .sig .lab{min-width:52px}
.fine{font-size:9.5px;line-height:14px;margin-top:9px}
.footer-band{position:absolute;left:0;top:1269px;width:1018px;height:50px;background:var(--orange);display:flex;align-items:center;justify-content:center;gap:20px;font-size:15px;color:#222}
.footer-band .item{display:flex;align-items:center;gap:8px}
</style>
</head>
<body>
<div class="stage">
  <div class="flyer">
    <section class="hero">
      <div class="hero-photo" role="img" aria-label="Sunlit rooftop terrace table with glasses of white wine, a cheese board and bread"></div>
      <h1 class="hero-title"><span class="nights">2 NIGHT</span> Hotel Stay</h1>
      <div class="gift-note">
        <svg viewBox="0 0 210 203" aria-hidden="true">
          <path d="M0 0 H210 V150 Q200 175 170 203 H0 Z" fill="#fff"/>
          <path d="M210 150 Q190 160 175 160 Q180 185 170 203 Q200 180 210 150 Z" fill="#dcdcdc"/>
        </svg>
        <div class="gift-note-text">
          <div>The Certificate is<br>Compliments of :</div>
          <div class="fields">NAME<br>PHONE NUMBER<br>E-MAIL ADDRESS</div>
        </div>
      </div>
    </section>

    <section class="boxed destinations">
      <h2 class="legend">Destinations Available :</h2>
      <p>Anaheim, CA--Atlanta, GA--Atlantic City, NJ--Branson, MO--Cancun, MX--Charleston, SC--Coeur d' Alene, ID--Daytona Beach, FL--Destin, FL--Ft. Lauderdale, FL--Ft. Meyers, FL--Gatlinburg, TN--Hilton Head, SC--Honolulu, HI--Kissimmee, FL--Lake Tahoe, CA--Las Vegas, NV--Myrtle Beach, SC--Niagara Falls/Buffalo Area, NY--Orlando, FL--Ormond Beach, FL--Palm Springs, CA--Pigeon Forge, TN--St. Petersburg, FL--San Antonio, TX--San Diego, CA--San Francisco, CA--Sedona, AZ--Sonoma Wine Country, CA--St. George, UT--Tampa, FL--Williamsburg, VA--Wisconsin Dells, WI--Tallahassee, FL--Augusta, GA--Columbia, SC--New York, NY--Florence, SC--Washington, D.C.--Chicago, IL--Salt Lake City, UT--Hollywood, CA-Dayton, OH--Tucson, AZ--Niagra Falls, ON/CAN--Seattle, WA--Portland, OR--Antioch, CA--San Mateo, CA--Brunswick, GA--Nashville, TN</p>
    </section>

    <section class="boxed terms">
      <h2 class="legend">Terms &amp; Conditions :</h2>
      <p>This certificate will be considered void if bartered or purchased for legal tender by the recipient. This certificate is valid for a reservation request form offering 2 adults 21 years of age and older plus up to 2 children under the age of 18, 2 nights of hotel accommodations in the city of their choice of available cities. The cost to activate this certificate to receive the reservation request form is just a one-time non-refundable $14.95 processing fee. The cost upon requesting reservations is just a tax &amp; fee deposit of $33 per night. Taxes &amp; fees usually range from $12-$33 per night depending on when and where you travel to. If the taxes &amp; fees are less than the $33 per night the difference will be refunded after travel is completed. 30 days advance reservation notice is required. In order to guarantee that you will show up to your booked reservation you will be required to pay a REFUNDABLE $50 "Reservation Guarantee Deposit". If you send in your travel dates, etc and you do not end up traveling then the reservation guarantee deposit will not be refundable. 7 days before and after holidays and conventions are not available. This offer is valid 7 days a week subject to availability. Friday and Saturday nights will require a surcharge of $20 per night. A $5 per person per night surcharge is enforced for each child up to 2 children under the age of 18. This offer is not valid for group travel. The recipient of this certificate is responsible for all expenses including but not limited to: transfers, food, gratuities, all pertinent fees, taxes, hotel surcharges, resort fees and any other miscellaneous expenses. If you activate this certificate online you will be able to instantly print your reservation request form. If you cannot print your own reservation request form we will mail it to you. You should receive it in the mail within 14 days. This certificate cannot be combined with any other promotional vacation offer. The expiration date on this certificate pertains only to activation of this certificate and not actual travel. You must activate this certificate by the expiration date printed on this certificate in order to receive the reservation request form. You must fill out the reservation request form with your destination choices and arrival dates and mail it to our fulfillment department within 6 months after activation, however travel can be completed within 12 months after activation. You will be required to give the travel agency multiple arrival dates and destinations. Only one 2 Night Hotel certificate Per Household Per Year. This certificate has no cash surrender value, void if discontinued and where prohibited by law. The terms of this offer are subject to change without notice. Do not rely upon representations other than what is printed on this certificate or the reservation request form. CST # 4018833</p>
    </section>

    <section class="order">
      <div class="redeem">
        <p class="intro">Simply fill out the form on this certificate and enclose payment of U.S. $14.95. Vantage, MeritCard, Amerix Pay, Discovia, Debit Card, Check Card, Check &amp; Money Orders are all accepted.</p>
        <h3>3 Ways To Redeem:</h3>
        <div class="step">1. For expedited redemption go to:</div>
        <div class="url">www.StayPerksForYou.com</div>
        <div class="step" style="margin-bottom:10px">2. Fax* certificate to: 1-888-555-0142</div>
        <div class="step">3. Mail* to:</div>
        <div class="addr">Redemption Center<br>4120 Harbor View Ave Ste B #210<br>Lakeside, Ca 92040</div>
        <div class="meta">
          <span>Certificate ID:</span><span class="val">10002</span>
          <span>Expiration Date:</span><span class="val expiry">04/08/2017</span>
        </div>
      </div>

      <div class="form-col billing">
        <h4>BILLING INFORMATION</h4>
        <div class="row"><span class="lab">Name:</span><span class="line"></span></div>
        <div class="row"><span class="lab">Address:</span><span class="line"></span></div>
        <div class="row"><span class="lab">City:</span><span class="line"></span></div>
        <div class="row"><span class="lab">State:</span><span class="line"></span></div>
        <div class="row"><span class="lab">Zip Code:</span><span class="line"></span></div>
        <div class="row"><span class="lab">Country:</span><span class="line"></span></div>
        <div class="row"><span class="lab">Phone:</span><span class="line"></span></div>
        <div class="row"><span class="lab">Email:</span><span class="line"></span></div>
        <h4 class="shipping-head">SHIPPING INFORMATION</h4>
        <div class="row"><span class="lab">Name:</span><span class="line"></span></div>
        <div class="row"><span class="lab">Address:</span><span class="line"></span></div>
        <div class="row"><span class="lab">City:</span><span class="line"></span></div>
        <div class="row"><span class="lab">State:</span><span class="line"></span></div>
        <div class="row"><span class="lab">Zip Code:</span><span class="line"></span></div>
        <div class="row"><span class="lab">Country:</span><span class="line"></span></div>
      </div>

      <div class="form-col payment">
        <h4>PAYMENT INFORMATION</h4>
        <div class="method-title">Payment Method:</div>
        <div class="methods">
          <span>Check</span><span>Money Order</span>
          <span>Vantage</span><span>MeritCard</span>
          <span>AMPX</span><span>Discovia Card</span>
        </div>
        <div class="row"><span class="lab">Name On Card:</span><span class="line"></span></div>
        <div class="row"><span class="lab">Card # (16 digits):</span><span class="line"></span></div>
        <div class="row expiry-row"><span class="lab">Expiration Date:</span><span class="short"></span><span class="slash">/</span><span class="line"></span></div>
        <div class="row"><span class="lab">CV2#**:</span><span class="line"></span></div>
        <div class="agree">I agree to terms and conditions</div>
        <div class="row sig"><span class="lab">Signature:</span><span class="line"></span></div>
        <div class="fine">"Redemption Center" will appear on your billing statement. Make checks and money orders payable to: "Redemption Center"<br>* You will receive your information by mail within 10 days.<br>** Last 3 digits on back of card (4 digits on front of AMPX).</div>
      </div>
    </section>

    <footer class="footer-band">
      <span class="item">
        <svg width="22" height="18" viewBox="0 0 22 18" aria-hidden="true"><path d="M11 1 L1 9.5 H4 V17 H9 V12 H13 V17 H18 V9.5 H21 Z" fill="#333"/></svg>
        The Redemption Center, 4120 Harbor View Ave Ste B #210, Lakeside, Ca 92040
      </span>
      <span class="item">
        <svg width="22" height="18" viewBox="0 0 22 18" aria-hidden="true"><circle cx="11" cy="9" r="7.5" fill="none" stroke="#333" stroke-width="2"/><path d="M3.5 9 H18.5 M11 1.5 Q6 9 11 16.5 M11 1.5 Q16 9 11 16.5" fill="none" stroke="#333" stroke-width="1.4"/></svg>
        www.StayPerksForYou.com
      </span>
    </footer>
  </div>
</div>
</body>
</html>
```